" Somos uma escola de Yoga e oferecemos aulas, Cursos de Formaçao para Professores de Yoga, workshops e retiros de meditaçao pelo Brasil e em países como Costa Rica, Panamá, Bali e Tailandia. Trabalhamos com o metodo Yin e Yang.. onde yin é a energia da meditaçao, contemplaçao e observaçao e yang do movimento, rítmo, força e atividade. "

```html
<!DOCTYPE html>
<html lang="pt-BR">
<head>
<meta charset="utf-8">
<title>Lua Sol Flow – Assinaturas de e-mail</title>
<link href="https://fonts.googleapis.com/css2?family=Arimo:wght@400;700&display=swap" rel="stylesheet">
<style>
  :root {
    --green: #8db13e;
    --green-light: #b5cf72;
    --grey: #7a7a7a;
    --ink: #2f2f2f;
    --white: #ffffff;
    --backdrop: #e9e9e6;
  }
  * { margin: 0; padding: 0; box-sizing: border-box; }
  html, body { width: 1200px; height: 1200px; overflow: hidden; }
  body {
    position: relative;
    background: var(--backdrop);
    font-family: "Arimo", Arial, sans-serif;
  }
  .signature {
    position: absolute;
    left: 115px;
    width: 972px;
    height: 220px;
    background: var(--white);
    overflow: hidden;
    box-shadow: 0 4px 14px rgba(0,0,0,.18);
  }
  .signature--full { top: 292px; }
  .signature--compact { top: 578px; }
  .signature__waves { position: absolute; inset: 0; width: 100%; height: 100%; }
  .person__name {
    position: absolute;
    font-weight: 700;
    font-size: 40px;
    line-height: 46px;
    color: var(--green);
    letter-spacing: -0.5px;
  }
  .person__role {
    position: absolute;
    font-weight: 700;
    font-size: 23px;
    line-height: 28px;
    color: var(--grey);
  }
  .contact {
    position: absolute;
    font-weight: 700;
    font-size: 16px;
    line-height: 22px;
    color: var(--green);
  }
  .signature--compact .contact { color: var(--white); font-size: 15px; line-height: 21px; }
  .brand {
    position: absolute;
    display: flex;
    flex-direction: column;
    align-items: center;
    gap: 8px;
  }
  .brand__mark { border-radius: 50%; background: var(--green); }
  .brand__name { font-weight: 400; color: var(--ink); white-space: nowrap; line-height: 1; }
  .showcase {
    position: absolute;
    left: 0; top: 880px;
    width: 1200px; height: 320px;
  }
  .showcase__waves { position: absolute; inset: 0; }
  .showcase .brand { left: 900px; width: 260px; top: 118px; }
  .showcase .brand__mark { background: var(--white); }
  .showcase .brand__name { color: var(--white); font-size: 40px; }
</style>
</head>
<body>

<section class="signature signature--full">
  <svg class="signature__waves" viewBox="0 0 972 220" preserveAspectRatio="none" aria-hidden="true">
    <path d="M0 188 C300 178 650 180 972 192 L972 197 C650 186 300 186 0 195 Z" fill="var(--green)"/>
    <path d="M0 206 C300 196 650 194 972 204 L972 220 L0 220 Z" fill="var(--green)"/>
  </svg>
  <h1 class="person__name" style="left:42px;top:36px;">Nome Sobrenome</h1>
  <p class="person__role" style="left:42px;top:84px;">Ccargo</p>
  <p class="contact" style="left:42px;top:116px;">
    Tel: +55 11 5550-1234 / +55 11 5550-5678<br>
    Email: luasolflow.com.br
  </p>
  <div class="brand" style="left:640px;top:26px;width:240px;">
    <span class="brand__mark" style="width:80px;height:80px;"></span>
    <span class="brand__name" style="font-size:32px;">lua sol flow</span>
  </div>
</section>

<section class="signature signature--compact">
  <svg class="signature__waves" viewBox="0 0 972 220" preserveAspectRatio="none" aria-hidden="true">
    <path d="M0 122 C300 136 620 176 972 150 L972 220 L0 220 Z" fill="var(--green)"/>
    <path d="M0 108 C300 122 620 164 972 136" fill="none" stroke="var(--green-light)" stroke-width="6"/>
    <path d="M0 130 C300 144 620 186 972 158" fill="none" stroke="var(--white)" stroke-width="3"/>
  </svg>
  <h1 class="person__name" style="left:22px;top:18px;">Nome Sobrenome</h1>
  <p class="person__role" style="left:22px;top:64px;">Ccargo</p>
  <p class="contact" style="left:22px;top:168px;">
    Tel: +55 11 5550-1234<br>
    Email: luasolflow.com.br
  </p>
  <div class="brand" style="left:660px;top:18px;width:220px;">
    <span class="brand__mark" style="width:64px;height:64px;"></span>
    <span class="brand__name" style="font-size:26px;">lua sol flow</span>
  </div>
</section>

<section class="showcase">
  <svg class="showcase__waves" viewBox="0 0 1200 320" width="1200" height="320" aria-hidden="true">
    <path d="M0 90 C300 150 600 200 850 130 C980 90 1100 30 1200 -20 L1200 320 L0 320 Z" fill="var(--green)"/>
    <path d="M0 110 C300 170 600 220 850 150 C980 110 1100 50 1200 0" fill="none" stroke="var(--white)" stroke-width="14"/>
    <path d="M0 140 C300 200 600 250 850 180 C980 140 1100 80 1200 30" fill="none" stroke="var(--green-light)" stroke-width="5"/>
  </svg>
  <div class="brand">
    <span class="brand__mark" style="width:84px;height:84px;"></span>
    <span class="brand__name">lua sol flow</span>
  </div>
</section>

</body>
</html>
```